Bref créative
Brochure for Geriatric Clinic
LumaCrest Residence & Geriatric SPA
Trifold (3 panel) brochure to be designed for a healthcare company specialized in assisted living facilities and geriatric rehabilitation.
We want to see the medical, the infrastructure and the nature rich enviroment aspects of our business in the design.
We want the brochure to communicate that our primary goal is to improve the quality of life for the senior and their families.
Specification of the folder
11" x 8.5"
279.4 mm x 215.9 mm
27.9 cm x 21.6 cm
3.7" x 8.5"
93.0 mm x 215.9 mm
9.3 cm x 21.6 cm
Please refer to our website at www.lumacrest-care.example, we provided a google translate menu at the bottom for the designers convenience. All pictures are free to use in this project.
Health
Personal, elderly, seniors an their families
Lumacrest logo
.ai format
LumaCrest document brief for brochure

```html
<!DOCTYPE html>
<html lang="en">
<head>
<meta charset="utf-8">
<title>LumaCrest Residence &amp; Geriatric SPA – Brochure Cover</title>
<link rel="stylesheet" href="https://fonts.googleapis.com/css2?family=Cormorant+Garamond:ital,wght@1,600&display=swap">
<style>
  :root {
    --backdrop: #d9dadb;
    --gold-light: #efe3a0;
    --gold-mid: #d9c369;
    --gold-deep: #b79a3c;
    --green-light: #8fbf3a;
    --green-mid: #4f8f22;
    --green-deep: #2c5d14;
    --cream: #f6efc9;
    --photo-top: #6e9a3c;
    --photo-mid: #4c6b2c;
    --photo-low: #8a7a66;
    --band: rgba(255, 255, 255, 0.55);
    --tagline: #b08f2e;
  }
  html, body {
    margin: 0;
    width: 1200px;
    height: 799px;
    overflow: hidden;
    background: var(--backdrop);
  }
  .canvas {
    position: relative;
    width: 1200px;
    height: 799px;
    display: flex;
    align-items: center;
    justify-content: center;
  }
  .cover-panel {
    position: relative;
    width: 322px;
    height: 740px;
    overflow: hidden;
    background: var(--gold-mid);
    box-shadow: 0 10px 30px rgba(0,0,0,0.18);
  }
  .cover-art {
    position: absolute;
    inset: 0;
    width: 100%;
    height: 100%;
  }
  .leaf-photo {
    position: absolute;
    left: 0;
    top: 300px;
    width: 100%;
    height: 440px;
    background:
      radial-gradient(ellipse at 70% 20%, #9cc552 0%, rgba(156,197,82,0) 45%),
      radial-gradient(ellipse at 25% 55%, #3f5e26 0%, rgba(63,94,38,0) 50%),
      linear-gradient(180deg, var(--photo-top) 0%, var(--photo-mid) 45%, var(--photo-low) 100%);
  }
  .brand {
    position: absolute;
    left: 0;
    right: 0;
    top: 58px;
    display: flex;
    align-items: center;
    justify-content: center;
    gap: 12px;
  }
  .brand-dot {
    width: 26px;
    height: 26px;
    border-radius: 50%;
    background: var(--green-deep);
  }
  .brand-name {
    font-family: "Cormorant Garamond", serif;
    font-style: italic;
    font-weight: 600;
    font-size: 40px;
    color: var(--green-deep);
    letter-spacing: 0.5px;
  }
  .tagline-band {
    position: absolute;
    left: 0;
    right: 0;
    top: 540px;
    height: 92px;
    background: var(--band);
    display: flex;
    flex-direction: column;
    align-items: center;
    justify-content: center;
  }
  .tagline {
    margin: 0;
    font-family: "Cormorant Garamond", serif;
    font-style: italic;
    font-weight: 600;
    font-size: 19px;
    line-height: 1.45;
    color: var(--tagline);
    text-align: center;
  }
</style>
</head>
<body>
<main class="canvas">
  <article class="cover-panel">
    <div class="leaf-photo" role="img" aria-label="Close-up photograph of fresh green leaves in a garden"></div>
    <svg class="cover-art" viewBox="0 0 322 740" preserveAspectRatio="none" aria-hidden="true">
      <defs>
        <linearGradient id="gold-field" x1="0" y1="0" x2="1" y2="1">
          <stop offset="0" stop-color="var(--gold-light)"/>
          <stop offset="0.55" stop-color="var(--gold-mid)"/>
          <stop offset="1" stop-color="var(--gold-deep)"/>
        </linearGradient>
        <linearGradient id="green-wave" x1="0" y1="0" x2="1" y2="0">
          <stop offset="0" stop-color="var(--green-deep)"/>
          <stop offset="0.5" stop-color="var(--green-mid)"/>
          <stop offset="1" stop-color="var(--green-light)"/>
        </linearGradient>
      </defs>
      <path class="gold-field" d="M0 0 H322 V150 C250 150 230 230 180 250 C120 275 60 240 0 250 Z" fill="url(#gold-field)"/>
      <path class="cream-stripe" d="M0 250 C60 240 120 275 180 250 C230 230 250 150 322 150 V168 C262 170 245 250 190 272 C125 298 60 262 0 272 Z" fill="var(--cream)"/>
      <path class="green-wave" d="M0 272 C60 262 125 298 190 272 C245 250 262 170 322 168 V300 C270 300 250 330 200 340 C140 352 70 320 0 330 Z" fill="url(#green-wave)"/>
    </svg>
    <div class="brand">
      <span class="brand-dot"></span>
      <span class="brand-name">LumaCrest</span>
    </div>
    <div class="tagline-band">
      <p class="tagline">Trusted health professionals<br>with a passion for quality</p>
    </div>
  </article>
</main>
</body>
</html>
```